TAVRO Capital Group LLC a High Risk Big Rewards company for Rich Young Entrepreneurs

We would like a very modern, powerful in the eyes of our customers, modern, minimalist feel, financial gain. this business card is for young Rich entrepreneurs who want to invest money into High Risk, Big Rewards Businesses. The card Should sell the business!! let your creativity go Wild! I pick most of the designers for this project because of your BOLD Designs, I would like this card to be Bold, Modern, Minimalist, use as many effects in your graphic Artist Mind, Do not let the Financial sound of this business to make you think Conservative that's the last thing we are! if you have a lot of money and you want to play a risky market call US
Updates

Project Deadline Extended
Reason: have not received, enough designs to choose 1st and second place, sure I have received over 100 designs but it seems most designers are submitting every card they have ever made before and calling it mine, please we are looking for fresh ideas please!

Target Market(s)

Private Risky Investors

Industry/Entity Type

Financial

Contact Information for Business Card

powerful in the eyes of our customers,modern, minimalist feel

Font styles to use
Other font styles liked:
• Modern feeling fonts

Requirements
Must have
• The Company Name is TAVRO Capital Group LLC and it must be on the CARD
• My Name, title, Cell , email
• Delvin Ashcroft G.E.D.
• Managing Member
• 555.038.6195
• delvin@tavrocapitalgroup.example
Nice to have
• try a black thick plastic card with round corners with Delvin Ashcroft GED (make sure GED is smaller than name) just on one side of the card, and my phone number with out the icons and email on the other side, this card should look like a exclusive credit card or exclusive VIP card, something you would never loose

```html
<!DOCTYPE html>
<html lang="en">
<head>
<meta charset="utf-8">
<title>TAVRO Capital Group LLC – Business Card</title>
<link href="https://fonts.googleapis.com/css2?family=Mulish:wght@300;400;600&display=swap" rel="stylesheet">
<style>
  :root {
    --stage: #e0426f;
    --card-black: #0b0b0b;
    --card-sheen: #262626;
    --ink-white: #f2f2f2;
    --ink-grey: #c9c9c9;
    --gold: #d9b866;
    --silver: #bfbfbf;
  }
  * { box-sizing: border-box; margin: 0; padding: 0; }
  html, body { width: 1200px; height: 1200px; overflow: hidden; }
  body {
    background: var(--stage);
    font-family: "Mulish", sans-serif;
    position: relative;
  }
  .card {
    position: absolute;
    left: 170px;
    width: 860px;
    height: 520px;
    border-radius: 44px;
    background:
      linear-gradient(160deg, var(--card-sheen) 0%, var(--card-black) 38%, var(--card-black) 100%);
    box-shadow: 0 18px 40px rgba(0,0,0,.35);
    overflow: hidden;
  }
  .card--front { top: 50px; }
  .card--back { top: 630px; }
  .card__art { position: absolute; inset: 0; width: 100%; height: 100%; }
  .ticks { stroke: var(--ink-grey); stroke-width: 22; stroke-dasharray: 1.6 6; fill: none; }
  .rule { stroke: var(--ink-white); stroke-width: 6; }
  .ring { fill: none; stroke: var(--silver); stroke-width: 9; }
  .text { position: absolute; color: var(--ink-white); white-space: nowrap; }
  .company { left: 150px; top: 118px; font-size: 31px; font-weight: 600; color: var(--gold); letter-spacing: .5px; }
  .person { left: 150px; top: 190px; font-size: 31px; font-weight: 300; color: var(--ink-grey); }
  .person__suffix { font-size: 17px; margin-left: 6px; }
  .role { left: 160px; top: 238px; font-size: 18px; font-weight: 400; color: var(--ink-grey); }
  .label { font-size: 22px; font-weight: 400; }
  .label--call { left: 95px; top: 322px; }
  .phone { left: 235px; top: 345px; font-size: 25px; font-weight: 300; letter-spacing: 1.5px; }
  .label--email { left: 95px; top: 400px; }
  .email { left: 200px; top: 428px; font-size: 25px; font-weight: 300; }
</style>
</head>
<body>

<section class="card card--front" aria-label="Card front">
  <svg class="card__art" viewBox="0 0 860 520" aria-hidden="true">
    <line class="ticks" x1="200" y1="0" x2="270" y2="0"/>
    <line class="ticks" x1="720" y1="0" x2="790" y2="0"/>
    <line class="ticks" x1="860" y1="60" x2="860" y2="130"/>
    <line class="ticks" x1="860" y1="330" x2="860" y2="400"/>
    <line class="ticks" x1="640" y1="520" x2="710" y2="520"/>
    <line class="ticks" x1="300" y1="520" x2="370" y2="520"/>
    <line class="ticks" x1="0" y1="360" x2="0" y2="430"/>
    <line class="ticks" x1="0" y1="150" x2="0" y2="220"/>
    <line class="rule" x1="300" y1="100" x2="830" y2="100"/>
    <line class="rule" x1="85" y1="178" x2="470" y2="178"/>
    <circle class="ring" cx="650" cy="270" r="82"/>
  </svg>
  <p class="text company">TAVRO Capital Group LLC</p>
  <p class="text person">Delvin Ashcroft<span class="person__suffix">GED</span></p>
  <p class="text role">Managing Member</p>
</section>

<section class="card card--back" aria-label="Card back">
  <svg class="card__art" viewBox="0 0 860 520" aria-hidden="true">
    <line class="ticks" x1="120" y1="0" x2="190" y2="0"/>
    <line class="ticks" x1="450" y1="0" x2="520" y2="0"/>
    <line class="ticks" x1="860" y1="90" x2="860" y2="160"/>
    <line class="ticks" x1="860" y1="360" x2="860" y2="430"/>
    <line class="ticks" x1="640" y1="520" x2="710" y2="520"/>
    <line class="ticks" x1="130" y1="520" x2="200" y2="520"/>
    <line class="ticks" x1="0" y1="120" x2="0" y2="190"/>
    <line class="ticks" x1="0" y1="330" x2="0" y2="400"/>
    <line class="rule" x1="40" y1="385" x2="560" y2="385"/>
    <line class="rule" x1="200" y1="478" x2="730" y2="478"/>
    <circle class="ring" cx="300" cy="180" r="82"/>
  </svg>
  <p class="text label label--call">Call</p>
  <p class="text phone">555.038.6195</p>
  <p class="text label label--email">Email</p>
  <p class="text email">delvin@tavrocapitalgroup.example</p>
</section>

</body>
</html>
```